K7 Solutions business card design contest. Use logo and create a professional layout.

See attached sample. Please sharpen all text and images, don't want any pix-elated content. We are looking for a clean look that quickly provides the information need. Please include our information provided on the sample card. Please feel free to offer any design changes. Please only user the colors provided: #2D3539 & #FFA500. Do not prefer any images other than the K7 Logo

Target Market(s)

Construction, Architects, General Contractors, residential

Industry/Entity Type

Business

Contact Information for Business Card

Company logo, Name, email, fax & phone

Font styles to use
Other font styles liked:
• Josefin Slab

Requirements
Must have
• Name
• Phone & Fax #'s
• address
• Logo
• Website url: www.kq7solutions.example
Nice to have
• Font Colors #2D3539 & #FFA400
• We prefer a white background.

```html
<!DOCTYPE html>
<html lang="en">
<head>
<meta charset="utf-8">
<title>K7 Solutions Business Card</title>
<link rel="stylesheet" href="https://fonts.googleapis.com/css2?family=Lato:wght@300;400;700&display=swap">
<style>
  :root {
    --page-bg: #e9e7e3;
    --card-white: #ffffff;
    --card-white-shade: #eeeeee;
    --ink: #2d3539;
    --ink-soft: #5a6266;
    --accent: #ffa500;
    --dark-card: #2d3539;
    --dark-card-deep: #1f2629;
    --on-dark: #ffffff;
    --rule: #4a5155;
  }
  * { margin: 0; padding: 0; box-sizing: border-box; }
  html, body { width: 1200px; height: 1023px; overflow: hidden; }
  body {
    background: var(--page-bg);
    font-family: "Lato", sans-serif;
    color: var(--ink);
    position: relative;
  }
  .card {
    position: absolute;
    width: 600px;
    height: 343px;
    border-radius: 18px;
    box-shadow: 0 10px 28px rgba(0,0,0,0.18);
    overflow: hidden;
  }
  .card-front {
    left: 40px;
    top: 70px;
    background: linear-gradient(160deg, var(--card-white) 55%, var(--card-white-shade));
  }
  .brand {
    position: absolute;
    left: 36px;
    top: 34px;
    display: flex;
    align-items: center;
    gap: 12px;
  }
  .brand-square {
    width: 40px;
    height: 40px;
    background: var(--ink);
    border-radius: 4px;
  }
  .brand-name {
    font-weight: 700;
    font-size: 30px;
    line-height: 1;
    color: var(--ink);
    letter-spacing: -0.3px;
  }
  .brand-tagline {
    font-weight: 700;
    font-size: 15px;
    color: var(--ink);
    margin-top: 2px;
  }
  .person {
    position: absolute;
    left: 36px;
    top: 190px;
    width: 300px;
  }
  .person-name {
    font-weight: 400;
    font-size: 17px;
    color: var(--ink-soft);
  }
  .person-title {
    font-weight: 300;
    font-size: 15px;
    color: var(--ink-soft);
    display: flex;
    align-items: flex-end;
    gap: 6px;
    margin-top: 2px;
  }
  .person-title::after {
    content: "";
    flex: 1;
    border-bottom: 1px solid var(--rule);
    margin-bottom: 4px;
  }
  .address {
    margin-top: 26px;
    font-weight: 300;
    font-size: 16px;
    line-height: 1.35;
    color: var(--ink-soft);
  }
  .divider {
    position: absolute;
    left: 350px;
    top: 40px;
    width: 1px;
    height: 250px;
    background: var(--rule);
  }
  .contact {
    position: absolute;
    right: 28px;
    top: 40px;
    list-style: none;
    text-align: right;
  }
  .contact li {
    display: flex;
    justify-content: flex-end;
    align-items: center;
    gap: 10px;
    font-weight: 400;
    font-size: 15px;
    line-height: 24px;
    color: var(--ink);
  }
  .contact-icon {
    width: 12px;
    height: 12px;
    flex: none;
  }
  .card-back {
    left: 560px;
    top: 590px;
    background: linear-gradient(150deg, #3a4448 0%, var(--dark-card) 45%, var(--dark-card-deep) 100%);
    display: flex;
    align-items: center;
    justify-content: center;
  }
  .back-brand {
    display: flex;
    align-items: center;
    gap: 20px;
  }
  .back-square {
    width: 66px;
    height: 66px;
    border: 3px solid var(--on-dark);
    border-radius: 6px;
  }
  .back-name {
    font-weight: 700;
    font-size: 52px;
    line-height: 1;
    color: var(--on-dark);
    letter-spacing: -0.5px;
  }
  .back-tagline {
    font-weight: 400;
    font-size: 22px;
    color: var(--on-dark);
    margin-top: 4px;
  }
</style>
</head>
<body>

<section class="card card-front" aria-label="Business card front">
  <div class="brand">
    <div class="brand-square"></div>
    <div>
      <div class="brand-name">K7 Solutions</div>
      <div class="brand-tagline">Clarity in Every Build</div>
    </div>
  </div>

  <div class="person">
    <p class="person-name">Marcus D. Holloway, MBA</p>
    <p class="person-title">Director of Operation</p>
    <p class="address">1270 Harlow Ridge Road, Suite 210-118<br>Fairbrook, Georgia, 30099</p>
  </div>

  <div class="divider"></div>

  <ul class="contact">
    <li>(555) 310-4827
      <svg class="contact-icon" viewBox="0 0 12 12" aria-hidden="true"><rect x="0.5" y="0.5" width="11" height="11" rx="2" fill="none" stroke="#ffa500"/></svg>
    </li>
    <li>(555) 310-4828
      <svg class="contact-icon" viewBox="0 0 12 12" aria-hidden="true"><rect x="0.5" y="0.5" width="11" height="11" rx="2" fill="none" stroke="#ffa500"/><rect x="3" y="3" width="6" height="6" fill="#ffa500"/></svg>
    </li>
    <li>info@kq7solutions.example
      <svg class="contact-icon" viewBox="0 0 12 12" aria-hidden="true"><rect width="12" height="12" rx="2" fill="#ffa500"/></svg>
    </li>
    <li>www.kq7solutions.example
      <svg class="contact-icon" viewBox="0 0 12 12" aria-hidden="true"><rect x="0.5" y="0.5" width="11" height="11" rx="2" fill="none" stroke="#ffa500"/></svg>
    </li>
  </ul>
</section>

<section class="card card-back" aria-label="Business card back">
  <div class="back-brand">
    <div class="back-square"></div>
    <div>
      <div class="back-name">K7 Solutions</div>
      <div class="back-tagline">Clarity in Every Build</div>
    </div>
  </div>
</section>

</body>
</html>
```